Naturopath specialising in Children's Health

I have just started working in a new clinic where I will be predominantly treating children so I would like to rebrand with a business card that reflects this.

I would like a clever design which is subtly playful and will attract children and parents alike, while maintaining a professional look. It must also reflect that I utilize natural medicine - including herbal medicine and nutrition as part of my treatment. Employing the use of a plant or herb would be ideal. I had envisioned the image of a dandelion blowing in the wind (or being blown by a child) as a great combination of the playful yet natural medicine I am trying to ecompass in the card.

I would like to use yellow, orange, blue or green as the dominant colour for the card.

The front of the card should contain the logo and the words 'Maribel Stroud - Naturopath.'

The back of the card should contain the following details:
Maribel Stroud BHSc Nat, Dip RM
Naturopath, Herbalist, Nutritionist, Iridologist, Remedial Massage Therapist, Reiki Practitioner
0417 382 961
Thistle Kenwick - (02) 9463 1508
maribel.stroud@fernmail.example
HWPA 47183

```html
<!DOCTYPE html>
<html lang="en">
<head>
<meta charset="utf-8">
<title>Maribel Stroud – Naturopath Business Card</title>
<link rel="stylesheet" href="https://fonts.googleapis.com/css2?family=Raleway:wght@300;400;500&display=swap">
<style>
  :root {
    --backdrop: #cbcbcb;
    --card-white: #ffffff;
    --leaf-green: #2fae3c;
    --leaf-green-light: #72c34c;
    --leaf-green-deep: #0ba64a;
    --blossom-orange: #f47a20;
    --text-light: #ffffff;
    --figure-green: #8fd46a;
  }
  * { box-sizing: border-box; margin: 0; padding: 0; }
  html, body {
    width: 1200px; height: 900px; overflow: hidden;
    background: var(--backdrop);
    font-family: "Raleway", Arial, sans-serif;
  }
  .stage {
    position: relative; width: 1200px; height: 900px;
    display: flex; align-items: center; justify-content: center; gap: 44px;
  }
  .card {
    position: relative; width: 530px; height: 320px;
    border-radius: 24px; overflow: hidden;
    box-shadow: 0 10px 24px rgba(0,0,0,0.18);
  }

  /* Front */
  .card-front { background: var(--card-white); }
  .card-front .frame {
    position: absolute; inset: 12px;
    border: 4px solid var(--leaf-green); border-radius: 18px;
  }
  .front-logo {
    position: absolute; left: 0; right: 0; top: 52px;
    display: flex; flex-direction: column; align-items: center;
  }
  .front-logo .figure-art {
    width: 110px; height: 100px; border-radius: 50px 50px 10px 10px;
    background: linear-gradient(160deg, var(--figure-green), var(--leaf-green));
  }
  .front-logo .brand-name {
    margin-top: 8px;
    font-size: 46px; font-weight: 400; color: var(--leaf-green);
    letter-spacing: 1px;
  }
  .front-logo .brand-role {
    margin-top: 4px;
    font-size: 20px; font-weight: 400; color: var(--blossom-orange);
    letter-spacing: 14px; padding-left: 14px;
  }

  /* Back */
  .card-back {
    background: linear-gradient(170deg, var(--leaf-green-light) 0%, var(--leaf-green-deep) 100%);
    color: var(--text-light);
  }
  .card-back .faint-figure {
    position: absolute; left: 18px; top: 60px; width: 170px; height: 260px;
    border-radius: 85px 85px 0 0;
    background: linear-gradient(180deg, rgba(255,255,255,0.14), rgba(255,255,255,0.04));
  }
  .contact {
    position: absolute; left: 110px; width: 310px; top: 30px;
    text-align: center;
  }
  .contact .full-name {
    font-size: 17px; font-weight: 400; color: var(--blossom-orange);
  }
  .contact .services {
    margin-top: 6px; font-size: 10.5px; font-weight: 300; line-height: 1.55;
  }
  .contact .mobile { margin-top: 14px; font-size: 18px; font-weight: 400; }
  .contact .clinic { margin-top: 16px; font-size: 14px; font-weight: 300; }
  .contact .clinic-phone { font-size: 18px; font-weight: 400; }
  .contact .email { margin-top: 16px; font-size: 12.5px; font-weight: 300; }
  .contact .membership { margin-top: 14px; font-size: 12px; font-weight: 300; }

  .back-logo {
    position: absolute; right: 22px; bottom: 40px; width: 150px;
    display: flex; flex-direction: column; align-items: center;
  }
  .back-logo .figure-art {
    width: 44px; height: 42px; border-radius: 22px 22px 6px 6px;
    background: linear-gradient(160deg, #ffffff, #dff5d6);
  }
  .back-logo .brand-name {
    margin-top: 4px; font-size: 19px; font-weight: 400; color: var(--text-light);
  }
  .back-logo .brand-role {
    font-size: 9px; font-weight: 400; color: var(--text-light);
    letter-spacing: 5px; padding-left: 5px;
  }
</style>
</head>
<body>
<main class="stage">
  <section class="card card-front" aria-label="Card front">
    <div class="frame"></div>
    <div class="front-logo">
      <div class="figure-art" role="img" aria-label="Green silhouette illustration of a person blowing an orange dandelion"></div>
      <div class="brand-name">Maribel Stroud</div>
      <div class="brand-role">Naturopath</div>
    </div>
  </section>

  <section class="card card-back" aria-label="Card back">
    <div class="faint-figure" role="img" aria-label="Faint silhouette illustration of a person blowing a dandelion"></div>
    <div class="contact">
      <p class="full-name">Maribel Stroud BHSc Nat, Dip RM</p>
      <p class="services">Naturopath, Herbalist, Nutritionist, Iridologist,<br>Remedial Massage Therapist, Reiki Practitioner</p>
      <p class="mobile">0417 382 961</p>
      <p class="clinic">Thistle Kenwick</p>
      <p class="clinic-phone">(02) 9463 1508</p>
      <p class="email">maribel.stroud@fernmail.example</p>
      <p class="membership">HWPA 47183</p>
    </div>
    <div class="back-logo">
      <div class="figure-art" role="img" aria-label="Small white silhouette illustration of a person blowing a dandelion"></div>
      <div class="brand-name">Maribel Stroud</div>
      <div class="brand-role">Naturopath</div>
    </div>
  </section>
</main>
</body>
</html>
```